Powerpoint Template Design using new logo

I am a consultant for the biotech and pharmaceutical industry. I need a simple but effective powerpoint template that I can use for my company deliverables. I would like the design of the powerpoint template to incorporate the symbol used in our logo (attached). The dominant colors should complement the logo as well.
Please use the standard powerpoint slide size - not the new widescreen format.

Target Market(s)

Pharmaceutical and biotech companies

Industry/Entity Type

Pharmaceutical

Font styles to use
Serif
Sans Serif

Requirements
Must have
• Must include logo (attached). Colors must complement logo.
I'd prefer a white background for the slides. Design should provide as much space as possible. I'd also like to have a place for a slide title at the top with a "takeaway" or "summary" box underneath. Then as much area as possible for me to provide project results.

```html
<!DOCTYPE html>
<html lang="en">
<head>
<meta charset="utf-8">
<title>Veridon Slide Template</title>
<link href="https://fonts.googleapis.com/css2?family=Roboto:ital,wght@0,300;0,400;0,700;1,400;1,700&display=swap" rel="stylesheet">
<style>
:root{
  --blue:#0a6bb6;
  --blue-dark:#0a5b9e;
  --blue-light:#15a3e0;
  --grey-bar:#999ea3;
  --bg:#a8aaad;
  --text:#7c7f83;
  --text-dark:#444;
  --line:#d8dbde;
  --white:#ffffff;
}
*{box-sizing:border-box;margin:0;padding:0}
html,body{width:1200px;height:898px;overflow:hidden}
body{background:var(--bg);font-family:"Roboto",Arial,sans-serif;position:relative;color:var(--text)}
.slide{position:absolute;width:357px;height:276px;background:var(--white);overflow:hidden}
.col1{left:41px}.col2{left:406px}.col3{left:771px}
.row1{top:24px}.row2{top:310px}.row3{top:595px}
.abs{position:absolute}
.header{position:absolute;left:0;top:0;width:100%;height:27px;background:var(--blue)}
.header h2{font-weight:300;font-size:13px;color:var(--white);position:absolute;left:12px;top:6px;letter-spacing:.2px}
.footer{position:absolute;left:11px;right:11px;top:258px;border-top:1px solid var(--line)}
.footer .brand{position:absolute;left:0;top:3px;font-size:9px;font-weight:700;color:var(--blue)}
.footer .page{position:absolute;right:0;top:-5px;font-size:4px;color:var(--text)}
.body-text{font-size:5.3px;line-height:1.75;color:var(--text);text-align:justify}
.body-text p+p{margin-top:6px}
/* Welcome */
.welcome{background:linear-gradient(135deg,#0e76c4,#0a5fa8)}
.welcome .helix{left:0;top:0;width:250px;height:210px;background:linear-gradient(120deg,rgba(255,255,255,.12),rgba(255,255,255,0) 70%)}
.welcome .intro{right:23px;top:130px;text-align:right;color:var(--white)}
.welcome .intro h1{font-weight:300;font-size:15.5px;line-height:1.25}
.welcome .intro .date{font-size:8px;font-weight:300;margin-top:5px}
.welcome .brand-band{left:0;top:212px;width:100%;height:34px;background:var(--white);border-top:1px solid #c9ccd0;border-bottom:1px solid #c9ccd0}
.welcome .brand-band span{position:absolute;left:20px;top:6px;font-size:21px;font-weight:700;color:var(--blue)}
/* About */
.lab-photo{left:11px;top:38px;width:335px;height:74px;background:linear-gradient(90deg,#f2f2f2 0%,#b0141c 18%,#f0f0f0 28%,#e2e800 40%,#17a63a 55%,#1d3fd6 72%,#c81a3a 90%,#eee 100%)}
.about-lead{left:11px;top:130px;width:110px;font-size:5.6px;line-height:1.65;color:var(--blue);text-transform:uppercase}
.about-copy{left:130px;top:130px;width:216px}
.summary-band{left:0;top:57px;width:100%;height:64px;background:var(--blue)}
.summary-band p{position:absolute;left:150px;right:12px;top:11px;font-size:6px;line-height:2.05;font-style:italic;color:var(--white);text-align:justify}
.team-photo{left:14px;top:47px;width:120px;height:80px;background:linear-gradient(120deg,#cfd8df,#8fa3b4 55%,#e7edf1)}
.about-right{left:149px;top:130px;width:196px}
/* Chart */
.chart{left:0;top:27px;width:357px;height:200px}
.year{font-size:9px;color:var(--blue);top:190px;width:40px;text-align:center}
.legend{top:211px;width:80px;font-size:4.5px;line-height:1.5;color:var(--text)}
.legend b{display:block;font-weight:400;font-size:5.5px;color:var(--text-dark)}
.legend i{display:inline-block;width:5px;height:5px;margin-right:3px;vertical-align:-1px}
/* Services */
.service{top:84px;width:100px;text-align:center}
.service .icon{width:42px;height:42px;border-radius:50%;margin:0 auto;background:var(--blue);display:flex;align-items:center;justify-content:center}
.service .icon.grey{background:var(--grey-bar)}
.service h3{font-size:8.5px;font-weight:400;color:var(--blue);margin-top:14px}
.service p{font-size:4.8px;line-height:1.6;margin-top:2px}
/* Team */
.team-intro{left:20px;right:20px;top:55px;text-align:center;font-size:5px;line-height:2.1;font-style:italic;font-weight:700;color:var(--text)}
.member{top:88px;width:80px;text-align:center}
.member .portrait{width:52px;height:52px;border-radius:50%;margin:0 auto;border:1.5px solid var(--blue);background:linear-gradient(160deg,#e4e6e8,#9a9fa4)}
.member h3{font-size:6.2px;font-weight:400;color:var(--blue);margin-top:12px;text-transform:uppercase}
.member .role{font-size:4.6px;font-style:italic;color:var(--text-dark)}
.member p{font-size:5px;line-height:2.05;text-align:justify;margin-top:9px}
/* Image text */
.image-text{background:var(--blue)}
.image-text .side-photo{left:178px;top:0;width:179px;height:276px;background:linear-gradient(160deg,#eef2f6,#b9cfe2 45%,#4e86c4 80%,#2b5fa8)}
.image-text h2{left:12px;top:18px;font-weight:300;font-size:13px;color:var(--white)}
.image-text .content{left:22px;top:96px;width:130px;color:var(--white)}
.image-text .content h3{font-size:5.8px;font-weight:400;margin-bottom:6px}
.image-text .content .body-text{color:var(--white)}
.image-text .brand{left:12px;top:262px;font-size:9px;font-weight:700;color:var(--white)}
/* Section */
.section{background:var(--blue)}
.section .badge{left:156px;top:114px;width:48px;height:48px;border-radius:50%;background:var(--white);display:flex;align-items:center;justify-content:center}
.section .rule{left:126px;top:170px;width:107px;border-top:1px solid rgba(255,255,255,.75)}
.section h2{left:0;width:100%;top:177px;text-align:center;font-weight:300;font-size:12px;color:var(--white)}
/* Closing */
.closing .top{left:0;top:0;width:100%;height:102px;background:var(--white)}
.closing .top span{position:absolute;left:20px;top:48px;font-size:28px;font-weight:700;color:var(--blue)}
.closing .bottom{left:0;top:102px;width:100%;height:174px;background:var(--blue)}
.closing h2{left:22px;top:121px;font-weight:300;font-size:13px;color:var(--white)}
.closing .sub{left:23px;top:139px;font-size:6px;color:var(--white)}
.contacts{left:23px;top:194px;list-style:none;color:var(--white);font-size:5.6px;line-height:1.3}
.contacts li{display:flex;align-items:flex-start;margin-bottom:8px}
.contacts svg{flex:none;margin-right:4px;margin-top:-1px}
</style>
</head>
<body>

<!-- Row 1 -->
<section class="slide col1 row1 welcome">
  <div class="abs helix" role="img" aria-label="Soft DNA double helix illustration"></div>
  <div class="abs intro">
    <h1>WELCOME<br>TO OUR PRESENTATION</h1>
    <div class="date">Birmingham, March 25, 2011</div>
  </div>
  <div class="abs brand-band"><span>VERIDON</span></div>
</section>

<section class="slide col2 row1">
  <header class="header"><h2>ABOUT US</h2></header>
  <div class="abs lab-photo" role="img" aria-label="Laboratory flasks filled with red, yellow, green and blue liquids"></div>
  <div class="abs about-lead">Lorem ipsum dolor sit met consectur adipsicing elit, sed do euismod tempor incididunt ut labore et delore magna</div>
  <div class="abs about-copy body-text">
    <p>Lorem ipsum dolor sit amet, consectetur adipisicing elit, sed do eiusmod tempor incididunt ut labore et dolore magna aliqua. Ut enim ad minim veniam, quis nostrud exercitation ullamco laboris nisi ut aliquip ex ea commodo consequat. Duis aute irure dolor in reprehenderit in voluptate velit esse cillum dolore eu fugiat nulla pariatur.</p>
    <p>Lorem ipsum dolor sit amet, consectetur adipisicing elit, sed do eiusmod tempor incididunt ut labore et dolore magna aliqua. Ut enim ad minim veniam, quis nostrud exercitation ullamco laboris nisi ut aliquip ex ea commodo consequat. Duis aute irure dolor in reprehenderit in voluptate velit esse cillum dolore eu</p>
  </div>
  <footer class="footer"><span class="brand">VERIDON</span><span class="page">2</span></footer>
</section>

<section class="slide col3 row1">
  <header class="header"><h2>ABOUT US</h2></header>
  <div class="abs summary-band"><p>Lorem ipsum dolor sit amet consectetur adipisicing elit, sed do eiusmod tempor incididunt ut labore et dolore magna aliqua. Ut enim ad</p></div>
  <div class="abs team-photo" role="img" aria-label="Scientist in mask and goggles examining a test tube"></div>
  <div class="abs about-right body-text" style="font-size:5px;line-height:1.8">
    <p>Lorem ipsum dolor sit amet, consectetur adipisicing elit, sed do eiusmod tempor incididunt ut labore et dolore magna aliqua. Ut enim ad minim veniam, quis nostrud exercitation ullamco laboris nisi ut aliquip ex ea commodo consequat. Duis aute irure dolor in reprehenderit in voluptate velit esse cillum dolore eu fugiat nulla pariatur.</p>
    <p>Lorem ipsum dolor sit amet, consectetur adipisicing elit, sed do eiusmod tempor incididunt ut labore et dolore magna aliqua. Ut enim ad minim veniam, quis nostrud exercitation ullamco laboris nisi ut aliquip ex ea commodo consequat. Duis aute irure dolor in reprehenderit in voluptate velit esse cillum dolore eu</p>
    <p>Fugiat nulla pariatur. Excepteur sint occaecat cupidatat non proident, sunt in culpa qui officia deserunt mollit anim id est laborum. Excepteur sint occaecat cupidatat non proident, sunt in consequat. Duis aute irure dolor in reprehenderit</p>
  </div>
  <footer class="footer"><span class="brand">VERIDON</span><span class="page">2</span></footer>
</section>

<!-- Row 2 -->
<section class="slide col1 row2">
  <header class="header"><h2>OUR CHART</h2></header>
  <svg class="abs" style="left:0;top:0" width="357" height="200" viewBox="0 0 357 200" aria-label="Bar chart by year">
    <g stroke="#555" stroke-width=".8">
      <line x1="63.2" y1="52" x2="63.2" y2="176"/>
      <line x1="63.2" y1="176" x2="279" y2="176"/>
      <line x1="60" y1="52" x2="63.2" y2="52"/><line x1="60" y1="72.7" x2="63.2" y2="72.7"/>
      <line x1="60" y1="93.3" x2="63.2" y2="93.3"/><line x1="60" y1="114" x2="63.2" y2="114"/>
      <line x1="60" y1="134.7" x2="63.2" y2="134.7"/><line x1="60" y1="155.3" x2="63.2" y2="155.3"/>
    </g>
    <g fill="var(--blue-dark)">
      <rect x="71.2" y="86.4" width="12.8" height="89.6"/><rect x="124" y="110.4" width="12.8" height="65.6"/>
      <rect x="177.6" y="95.2" width="12.8" height="80.8"/><rect x="231.2" y="98.4" width="12.8" height="77.6"/>
    </g>
    <g fill="var(--grey-bar)">
      <rect x="84" y="126.4" width="12.8" height="49.6"/><rect x="136.8" y="86.4" width="12.8" height="89.6"/>
      <rect x="190.4" y="136.8" width="12.8" height="39.2"/><rect x="244" y="128" width="12.8" height="48"/>
    </g>
    <g fill="var(--blue-light)">
      <rect x="96.8" y="134.4" width="12.8" height="41.6"/><rect x="149.6" y="134.4" width="12.8" height="41.6"/>
      <rect x="203.2" y="119.2" width="12.8" height="56.8"/><rect x="256.8" y="89.6" width="12.8" height="86.4"/>
    </g>
  </svg>
  <span class="abs year" style="left:71px">2009</span>
  <span class="abs year" style="left:124px">2010</span>
  <span class="abs year" style="left:178px">2011</span>
  <span class="abs year" style="left:232px">2012</span>
  <div class="abs legend" style="left:44px"><b><i style="background:var(--blue-dark)"></i>LOREM IPSUM</b>Lorem ipsum dolor sit amet, consectetur adipisicing elit, sed do eiusmod tempor incididunt ut labore et dolore magna</div>
  <div class="abs legend" style="left:143px"><b><i style="background:var(--grey-bar)"></i>LOREM IPSUM</b>Lorem ipsum dolor sit amet, consectetur adipisicing elit, sed do eiusmod tempor incididunt ut labore et dolore magna</div>
  <div class="abs legend" style="left:238px"><b><i style="background:var(--blue-light)"></i>LOREM IPSUM</b>Lorem ipsum dolor sit amet, consectetur adipisicing elit, sed do eiusmod tempor incididunt ut labore et dolore magna</div>
  <footer class="footer"><span class="brand">VERIDON</span><span class="page">2</span></footer>
</section>

<section class="slide col2 row2">
  <header class="header"><h2>OUR SERVICES</h2></header>
  <div class="abs service" style="left:15px">
    <div class="icon"><svg width="22" height="22" viewBox="0 0 24 24"><g fill="#fff"><circle cx="12" cy="12" r="7"/><g stroke="#fff" stroke-width="3"><line x1="12" y1="2" x2="12" y2="22"/><line x1="2" y1="12" x2="22" y2="12"/><line x1="5" y1="5" x2="19" y2="19"/><line x1="19" y1="5" x2="5" y2="19"/></g></g><circle cx="12" cy="12" r="3" fill="var(--blue)"/></svg></div>
    <h3>OUR SERVICES</h3>
    <p>dolor sit amet, consectetur adipisicing elit, sed do eiusmod tempor incididunt ut labore et dolore magna aliqua. Ut enim ad minim veniam, quis nostrud exercitation ullamco laboris nisi ut aliquip ex ea cesse cillum dolore eu fugiat nulla pariatur.</p>
  </div>
  <div class="abs service" style="left:128px">
    <div class="icon grey"><svg width="22" height="22" viewBox="0 0 24 24" fill="none" stroke="#fff" stroke-width="2"><path d="M10 3h4v9h-4z"/><path d="M7 20h11M12 12v4M8 16a6 6 0 0 0 9 0"/></svg></div>
    <h3>OUR SERVICES</h3>
    <p>dolor sit amet, consectetur adipisicing elit, sed do eiusmod tempor incididunt ut labore et dolore magna aliqua. Ut enim ad minim veniam, quis nostrud exercitation ullamco laboris nisi ut aliquip ex ea cesse cillum dolore eu fugiat nulla pariatur.</p>
  </div>
  <div class="abs service" style="left:237px">
    <div class="icon"><svg width="22" height="22" viewBox="0 0 24 24" fill="none" stroke="#fff" stroke-width="2"><rect x="3" y="4" width="18" height="11"/><path d="M12 15v3M8 21l4-3 4 3M8 9h8"/></svg></div>
    <h3>OUR SERVICES</h3>
    <p>dolor sit amet, consectetur adipisicing elit, sed do eiusmod tempor incididunt ut labore et dolore magna aliqua. Ut enim ad minim veniam, quis nostrud exercitation ullamco laboris nisi ut aliquip ex ea cesse cillum dolore eu fugiat nulla pariatur.</p>
  </div>
  <footer class="footer"><span class="brand">VERIDON</span><span class="page">2</span></footer>
</section>

<section class="slide col3 row2">
  <header class="header"><h2>OUR TEAM</h2></header>
  <p class="abs team-intro">dolor sit amet, consectetur adipisicing elit, sed do eiusmod tempor incididunt ut labore et dolore magna aliqua.<br>Ut enim ad minim veniam, quis nostrud exercitation ullamco laboris nisi ut a</p>
  <div class="abs member" style="left:34px">
    <div class="portrait" role="img" aria-label="Portrait photo of team member"></div>
    <h3>Arlen Voss</h3><div class="role">President</div>
    <p>dolor sit amet, consectetur adipisicing elit, sed do eiusmod tempor incididunt ut labore et dolore magna aliqua. Ut enim ad minim veniam, quis nostrud exercitation</p>
  </div>
  <div class="abs member" style="left:137px">
    <div class="portrait" role="img" aria-label="Portrait photo of team member"></div>
    <h3>Mira Castell</h3><div class="role">CEO / Founder</div>
    <p>dolor sit amet, consectetur adipisicing elit, sed do eiusmod tempor incididunt ut labore et dolore magna aliqua. Ut enim ad minim veniam, quis nostrud exercitation</p>
  </div>
  <div class="abs member" style="left:237px">
    <div class="portrait" role="img" aria-label="Portrait photo of team member"></div>
    <h3>Lena Hartwig</h3><div class="role">Vice President</div>
    <p>dolor sit amet, consectetur adipisicing elit, sed do eiusmod tempor incididunt ut labore et dolore magna aliqua. Ut enim ad minim veniam, quis nostrud exercitation</p>
  </div>
  <footer class="footer"><span class="brand">VERIDON</span><span class="page">2</span></footer>
</section>

<!-- Row 3 -->
<section class="slide col1 row3 image-text">
  <div class="abs side-photo" role="img" aria-label="Researcher in safety goggles using a pipette over blue test tubes"></div>
  <h2 class="abs">IMAGE TEXT</h2>
  <div class="abs content">
    <h3>LOREM IPSUM DOLOR SIT MET</h3>
    <div class="body-text">
      <p>Lorem ipsum dolor sit amet, consectetur adipisicing elit, sed do eiusmod tempor incididunt ut labore et dolore magna aliqua. Ut enim ad minim veniam, quis nostrud exercitation ullamco laboris nisi ut aliquip ex ea commodo consequat. Duis aute irure dolor in reprehenderit in voluptate velit esse cillum dolore eu fugiat nulla pariatur.</p>
      <p>Lorem ipsum dolor sit amet, consectetur adipisicing elit, sed do eiusmod tempor incididunt ut labore et dolore magna aliqua. Ut enim ad minim veniam, quis nostrud exercitation ullamco laboris nisi ut aliquip ex ea commodo consequat. Duis aute irure dolor in reprehenderit in voluptate velit esse cillum dolore eu</p>
    </div>
  </div>
  <span class="abs brand">VERIDON</span>
</section>

<section class="slide col2 row3 section">
  <div class="abs badge"><svg width="28" height="28" viewBox="0 0 24 24"><path d="M15 2l7 7-1.5 1.5-1-1L10 19a4 4 0 0 1-5.7-5.7L14 3.5l-.5-.5z" fill="var(--blue)"/><circle cx="9" cy="5" r="1" fill="var(--blue)"/><circle cx="6" cy="8" r=".8" fill="var(--blue)"/><circle cx="11" cy="2.5" r=".7" fill="var(--blue)"/></svg></div>
  <div class="abs rule"></div>
  <h2 class="abs">SECTION TITLE</h2>
</section>

<section class="slide col3 row3 closing">
  <div class="abs top"><span>VERIDON</span></div>
  <div class="abs bottom"></div>
  <h2 class="abs">THANK YOU</h2>
  <div class="abs sub">FOR YOUR TIME</div>
  <ul class="abs contacts">
    <li><svg width="8" height="8" viewBox="0 0 10 10"><circle cx="5" cy="5" r="5" fill="#fff"/><path d="M5 2a2 2 0 0 0-2 2c0 1.5 2 4 2 4s2-2.5 2-4a2 2 0 0 0-2-2z" fill="var(--blue)"/></svg><span>4120 Harbor Crest Way Ste 300<br>Fairview, Ohio 44126</span></li>
    <li><svg width="8" height="8" viewBox="0 0 10 10"><circle cx="5" cy="5" r="5" fill="#fff"/><path d="M3 3h4v1H6v3H4V4H3z" fill="var(--blue)"/></svg><span>1.800.555.0148</span></li>
    <li><svg width="8" height="8" viewBox="0 0 10 10"><circle cx="5" cy="5" r="5" fill="#fff"/><rect x="2.5" y="3.2" width="5" height="3.6" fill="var(--blue)"/><path d="M2.5 3.2L5 5.2l2.5-2" stroke="#fff" stroke-width=".6" fill="none"/></svg><span>support@veridon.com</span></li>
    <li><svg width="8" height="8" viewBox="0 0 10 10"><circle cx="5" cy="5" r="5" fill="#fff"/><circle cx="5" cy="5" r="2.6" fill="none" stroke="var(--blue)" stroke-width=".8"/><path d="M2.4 5h5.2M5 2.4v5.2" stroke="var(--blue)" stroke-width=".6"/></svg><span>www.veridon.com</span></li>
  </ul>
</section>

</body>
</html>
```